Design Business Cards for Pinecrest Holdings & Freight Company

Dear Designers,

We are looking for a Clean, Classy, Unique, Luxury and professional design for business cards & simple letter head for a Pinecrest Holdings & Freight. Please see the attached image for our logo. We like the black on the side of the card, but by all means be creative. You can also play around with the logo.
We prefer gold foil stamping, but it is not really necessary.

Feel free to submit as many entries as you want to increase your chance of winning. DO NOT submit something we can actually do it ourselves, e.g. free online generator, copying and pasting our logo on somehing plain without actually designing anything

For Business Card

• The card will be double sided with following detail appear.

-Name,
-Position,
-Address,
-Phone number,
-Email address
-and Website URL
• Business Card size, direction(horizontal or vertical) & shape is open to designer creativity.

For Letterhead
Design
• Should be matching colour theme of Logo/Business card.

Others;
• Winner need to provide layered PSD & ai files for all designs including fonts, colours used and any additional related documents and files.
• Attached is the logo (must be used in design)
• Building a website and brochures that will be further selling points to the winner, for our next business development.

Thanks for all your entries!

```html
<!DOCTYPE html>
<html lang="en">
<head>
<meta charset="utf-8">
<title>Pinecrest Holdings &amp; Freight – Business Card</title>
<link href="https://fonts.googleapis.com/css2?family=Questrial&display=swap" rel="stylesheet">
<style>
  :root {
    --backdrop: #9a9a9a;
    --card: #262626;
    --gold: #f5b60a;
    --gold-soft: #e2a615;
    --bronze: #8a4a12;
    --olive: #6b5a1a;
    --label: #ffffff;
  }
  html, body {
    margin: 0;
    padding: 0;
    overflow: hidden;
  }
  .canvas {
    position: relative;
    width: 960px;
    height: 1200px;
    background: var(--backdrop);
    overflow: hidden;
    font-family: "Questrial", "Century Gothic", sans-serif;
  }
  .card {
    position: absolute;
    top: 320px;
    height: 691px;
    background: var(--card);
    overflow: hidden;
  }
  .card--front { left: 19px; width: 461px; }
  .card--back { left: 485px; width: 459px; }

  .card__band {
    position: absolute;
    left: 0;
    right: 0;
    bottom: 0;
    height: 37px;
    background: var(--gold);
  }
  .card--back .card__band { background: var(--gold-soft); }

  .corner {
    position: absolute;
    top: 0;
    width: 24px;
    height: 24px;
    display: block;
  }
  .corner--left { left: 0; }
  .corner--right { right: 0; }

  .stripes-horizontal {
    position: absolute;
    left: 0;
    top: 545px;
    width: 461px;
    height: 52px;
    display: block;
  }
  .stripes-vertical {
    position: absolute;
    left: 358px;
    top: 0;
    width: 56px;
    height: 654px;
    display: block;
  }

  .brand-name {
    position: absolute;
    left: 0;
    right: 0;
    top: 355px;
    margin: 0;
    text-align: center;
    color: var(--gold);
    font-size: 38px;
    font-weight: 400;
    line-height: 1.25;
  }

  .contact {
    position: absolute;
    left: 0;
    width: 426px;
    top: 176px;
    margin: 0;
    text-align: center;
    font-size: 21px;
    line-height: 26.8px;
  }
  .contact dt { color: var(--label); margin: 0; }
  .contact dd { color: var(--gold); margin: 0; }
</style>
</head>
<body>
<div class="canvas">

  <section class="card card--front">
    <svg class="corner corner--left" viewBox="0 0 24 24" aria-hidden="true"><polygon points="0,0 24,0 0,24" fill="var(--gold)"/></svg>
    <svg class="corner corner--right" viewBox="0 0 24 24" aria-hidden="true"><polygon points="0,0 24,0 24,24" fill="var(--gold)"/></svg>

    <h1 class="brand-name">Pinecrest Holdings<br>&amp; Freight</h1>

    <svg class="stripes-horizontal" viewBox="0 0 461 52" aria-hidden="true">
      <rect x="0" y="0" width="461" height="4" fill="var(--gold)"/>
      <rect x="0" y="11" width="461" height="4" fill="var(--olive)"/>
      <rect x="0" y="23" width="461" height="5" fill="var(--bronze)"/>
      <rect x="0" y="36" width="461" height="4" fill="var(--olive)"/>
      <rect x="0" y="48" width="461" height="4" fill="var(--gold)"/>
    </svg>

    <div class="card__band"></div>
  </section>

  <section class="card card--back">
    <dl class="contact">
      <dt>Name :</dt>
      <dd>Elias Marwood</dd>
      <dt>Position :</dt>
      <dd>CEO</dd>
      <dt>Address :</dt>
      <dd>12 Harbour Lane England</dd>
      <dt>Phone number :</dt>
      <dd>01632960418</dd>
      <dt>Email address :</dt>
      <dd>info@pinecrestmail.com</dd>
      <dt>Website URL :</dt>
      <dd>www.pinecrestfreight.com</dd>
    </dl>

    <svg class="stripes-vertical" viewBox="0 0 56 654" aria-hidden="true">
      <rect x="0" y="0" width="5" height="654" fill="var(--gold)"/>
      <rect x="11" y="0" width="4" height="654" fill="var(--olive)"/>
      <rect x="21" y="0" width="5" height="654" fill="var(--bronze)"/>
      <rect x="32" y="0" width="4" height="654" fill="var(--gold-soft)"/>
      <rect x="41" y="0" width="4" height="654" fill="var(--bronze)"/>
      <rect x="50" y="0" width="5" height="654" fill="var(--gold)"/>
    </svg>

    <div class="card__band"></div>
  </section>

</div>
</body>
</html>
```